make it look old timey and motherly but mordern...bath soak with cooling vapors. tall pine hush

need a bath soak label...cooling vapors. will be in a pouch like below. dont pay attention to the design, just attatching so you know the kind of pouch itll be in. need something trusty, minimal and clean...its called tall pine hush bath soak the best bath yull ever take.... for sore muscles, cooling vapors, smells good...made with menthol lemon and eucalyptus...give me something good.

Target Market(s)

make it look old timey and motherly but mordern

Font styles to use
Serif
Sans Serif

Colors
0054AA
0677BA
7BADD7
CADEEF
E8F1F8
0094D4
00A9DD
6FCCEA
C7EBF8
E9F6FB
FFF300
FFF600
FEFA6F
FFFEC7
FFFEE8
FFC000
F8CF3A
FAE287
FDF2CF
FEFAEE
E54698
E96AAD
F1A4CE
F9D9EA
FCEFF6
6B429C
8869AF
B7A5CE
E3DAEB
F3F0F8

```html
<!DOCTYPE html>
<html lang="en">
<head>
<meta charset="UTF-8">
<title>Tall Pine Hush Bath Soak — Pouch Label</title>
<link href="https://fonts.googleapis.com/css2?family=Lexend:wght@500&family=Montserrat:wght@400;500&family=Dancing+Script:wght@700&display=swap" rel="stylesheet">
<style>
  :root {
    --stage: #969696;
    --pink: #d8469f;
    --pink-deep: #c8338f;
    --navy: #1f4f9c;
    --blush-top: #dfc0da;
    --mist: #e4e0e4;
    --mint: #b5d9c1;
    --mint-deep: #8ec6a2;
    --pattern: #d5aed0;
    --white: #ffffff;
  }
  * { margin: 0; padding: 0; box-sizing: border-box; }
  html, body { width: 1200px; height: 800px; overflow: hidden; }
  body { background: var(--stage); position: relative; }

  .label {
    position: absolute;
    left: 359px; top: 20px;
    width: 482px; height: 760px;
    border-radius: 18px;
    overflow: hidden;
    background: linear-gradient(180deg, var(--blush-top) 0%, var(--mist) 40%, var(--mint) 72%, var(--mint-deep) 100%);
    text-align: center;
    color: var(--navy);
  }
  .leaf-band {
    position: absolute; left: 0; top: 0; width: 100%; height: 126px;
    background: linear-gradient(180deg, var(--pattern) 0%, rgba(213,174,208,0) 100%);
    opacity: .55;
  }
  .tear-line {
    position: absolute; left: 0; top: 51px; width: 100%; height: 2px;
    background: var(--pink-deep);
  }
  .badge {
    position: absolute; left: 50%; top: 36px; transform: translateX(-50%);
    width: 131px; height: 35px; border-radius: 18px;
    background: var(--pink-deep); color: var(--white);
    font: 500 14px/15px "Lexend", sans-serif;
    display: flex; align-items: center; justify-content: center;
    letter-spacing: .3px;
  }
  .title {
    position: absolute; left: 0; width: 100%; top: 150px;
    font: 500 41px/42px "Lexend", sans-serif;
    color: var(--pink);
    letter-spacing: .5px;
  }
  .tagline {
    position: absolute; left: 0; width: 100%; top: 238px;
    font: 400 20px/1 "Montserrat", sans-serif;
    color: var(--navy);
  }
  .benefits { position: absolute; left: 0; width: 100%; top: 350px; }
  .benefit-sore {
    font: 400 27px/34px "Montserrat", sans-serif; color: var(--pink);
  }
  .benefit-vapors {
    font: 500 28px/36px "Montserrat", sans-serif; color: var(--navy);
    letter-spacing: .5px;
  }
  .benefit-scent {
    font: 700 38px/42px "Dancing Script", cursive; color: var(--pink-deep);
  }
  .botanicals {
    position: absolute; left: 164px; top: 540px; width: 143px; height: 82px;
    border-radius: 40px;
    background: radial-gradient(ellipse at center, rgba(31,79,156,.22) 0%, rgba(31,79,156,.06) 75%, rgba(31,79,156,0) 100%);
  }
  .ingredients {
    position: absolute; left: 0; width: 100%; top: 630px;
    font: 500 14px/16px "Montserrat", sans-serif; color: var(--navy);
  }
  .net-weight {
    position: absolute; left: 0; width: 100%; top: 711px;
    font: 500 10px/1 "Montserrat", sans-serif; color: var(--navy);
  }
</style>
</head>
<body>
  <main class="label">
    <div class="leaf-band" role="img" aria-label="Faint outlined leaf pattern across the top band"></div>
    <div class="tear-line"></div>
    <div class="badge">Natural<br>Ingredients</div>

    <h1 class="title">tall pine hush<br>best bath soak</h1>
    <p class="tagline">The best bath yull ever take</p>

    <section class="benefits">
      <p class="benefit-sore">For sore muscles</p>
      <p class="benefit-vapors">COOLING VAPORS</p>
      <p class="benefit-scent">Smells good</p>
    </section>

    <div class="botanicals" role="img" aria-label="Line illustration of a lemon slice, mint leaves and a eucalyptus sprig"></div>
    <p class="ingredients">Menthol, Lemon<br>and Eucalyptus</p>
    <p class="net-weight">NW 15 oz (425 grs)</p>
  </main>
</body>
</html>
```